Strong, modern, clean Business Card design

Looking for a stunning, but CLEAN business card design. While we are a faith-based organization, we do NOT want this to look religious.

Industry/Entity Type

Non-Profit

Contact Information for Business Card

Mark Dalton | Lead Pastor
mark@BraverHollow.org
555-218-9034
PO Box 7183
Millbrook, CO 80612

Font styles to use
Serif
Sans Serif

Requirements
Should not have
• Religious imagery or symbolism

```html
<!DOCTYPE html>
<html lang="en">
<head>
<meta charset="utf-8">
<title>Braver Hollow Church – Business Card</title>
<link rel="stylesheet" href="https://fonts.googleapis.com/css2?family=Cinzel:wght@400;700&family=Tinos&display=swap">
<style>
  :root {
    --brand-blue: #4b7b97;
    --card-white: #ffffff;
    --stage: #e7e9eb;
    --rule: #9fb6c4;
  }
  * { box-sizing: border-box; margin: 0; padding: 0; }
  html, body { width: 1200px; height: 902px; overflow: hidden; }
  body {
    background: var(--stage);
    position: relative;
    font-family: "Tinos", "Times New Roman", serif;
  }
  .card {
    position: absolute;
    left: 280px;
    width: 640px;
    height: 366px;
    border-radius: 26px;
    overflow: hidden;
    box-shadow: 0 6px 18px rgba(0,0,0,0.12);
  }
  /* Back side */
  .card-back {
    top: 50px;
    background: var(--brand-blue);
    display: flex;
    align-items: center;
    justify-content: center;
  }
  .back-name {
    font-family: "Cinzel", Georgia, serif;
    font-weight: 400;
    color: var(--card-white);
    font-size: 42px;
    letter-spacing: 4px;
  }
  /* Front side */
  .card-front {
    top: 466px;
    background: var(--card-white);
  }
  .identity {
    position: absolute;
    top: 0; left: 0; right: 0;
    height: 226px;
    display: flex;
    flex-direction: column;
    align-items: center;
    justify-content: center;
    color: var(--brand-blue);
    text-align: center;
  }
  .org-name {
    font-family: "Cinzel", Georgia, serif;
    font-weight: 700;
    font-size: 38px;
    line-height: 1;
    letter-spacing: 2px;
  }
  .org-type {
    font-family: "Cinzel", Georgia, serif;
    font-size: 20px;
    line-height: 1;
    letter-spacing: 22px;
    margin: 6px 0 0 22px;
  }
  .divider {
    width: 370px;
    height: 1px;
    background: var(--rule);
    margin: 12px 0 12px;
    position: relative;
  }
  .divider::after {
    content: "";
    position: absolute;
    left: 50%; top: -2px;
    width: 5px; height: 5px;
    margin-left: -2.5px;
    border-radius: 50%;
    background: var(--brand-blue);
  }
  .person-name {
    font-family: "Cinzel", Georgia, serif;
    font-weight: 700;
    font-size: 24px;
    line-height: 1.1;
    letter-spacing: 2px;
  }
  .person-title {
    font-family: "Cinzel", Georgia, serif;
    font-size: 12px;
    letter-spacing: 5px;
    margin: 3px 0 0 5px;
  }
  .contact-band {
    position: absolute;
    left: 0; right: 0; bottom: 0;
    height: 140px;
    background: var(--brand-blue);
    display: flex;
    align-items: center;
  }
  .contact-item {
    flex: 1 1 0;
    display: flex;
    flex-direction: column;
    align-items: center;
    gap: 10px;
    color: var(--card-white);
    font-size: 15px;
    white-space: nowrap;
    text-align: center;
    position: relative;
  }
  .contact-item.address { flex-grow: 1.45; }
  .contact-item + .contact-item::before {
    content: "";
    position: absolute;
    left: 0; top: 4px;
    width: 1px; height: 62px;
    background: rgba(255,255,255,0.35);
  }
  .contact-icon { width: 34px; height: 34px; }
</style>
</head>
<body>

<section class="card card-back" aria-label="Card back">
  <span class="back-name">BRAVER HOLLOW</span>
</section>

<section class="card card-front" aria-label="Card front">
  <div class="identity">
    <div class="org-name">BRAVER HOLLOW</div>
    <div class="org-type">CHURCH</div>
    <div class="divider"></div>
    <div class="person-name">MARK DALTON</div>
    <div class="person-title">LEAD PASTOR</div>
  </div>

  <div class="contact-band">
    <div class="contact-item">
      <svg class="contact-icon" viewBox="0 0 34 34" aria-hidden="true">
        <circle cx="17" cy="17" r="15.5" fill="none" stroke="#fff" stroke-width="1.6"/>
        <rect x="12" y="8" width="10" height="18" rx="1.5" fill="none" stroke="#fff" stroke-width="1.5"/>
        <rect x="13.8" y="10.5" width="6.4" height="5" fill="#fff"/>
        <g fill="#fff"><rect x="14" y="18" width="1.6" height="1.4"/><rect x="16.2" y="18" width="1.6" height="1.4"/><rect x="18.4" y="18" width="1.6" height="1.4"/><rect x="14" y="20.6" width="1.6" height="1.4"/><rect x="16.2" y="20.6" width="1.6" height="1.4"/><rect x="18.4" y="20.6" width="1.6" height="1.4"/></g>
      </svg>
      <span>555-218-9034</span>
    </div>
    <div class="contact-item">
      <svg class="contact-icon" viewBox="0 0 34 34" aria-hidden="true">
        <circle cx="17" cy="17" r="15.5" fill="none" stroke="#fff" stroke-width="1.6"/>
        <rect x="9" y="11.5" width="16" height="11" fill="#fff"/>
        <path d="M9 11.5 L17 18 L25 11.5" fill="none" stroke="#4b7b97" stroke-width="1.4"/>
      </svg>
      <span>mark@BraverHollow.org</span>
    </div>
    <div class="contact-item address">
      <svg class="contact-icon" viewBox="0 0 34 34" aria-hidden="true">
        <circle cx="17" cy="17" r="15.5" fill="none" stroke="#fff" stroke-width="1.6"/>
        <path d="M17 26 C13 20.5 11.5 17.5 11.5 14.5 A5.5 5.5 0 0 1 22.5 14.5 C22.5 17.5 21 20.5 17 26 Z" fill="none" stroke="#fff" stroke-width="1.6"/>
        <circle cx="17" cy="14.5" r="2" fill="#fff"/>
      </svg>
      <span>PO Box 7183, Millbrook, CO 80612</span>
    </div>
  </div>
</section>

</body>
</html>
```